Christmas / Holiday themed front and back wine label set
Warm Mulled Wine / hot spiced wine
We need a hot spice wine label that screams Christmas / Thanksgiving / the holidays. Need a front and back label set. Label needs to be obvious holiday themed so retailers can display / sell for the Christmas holiday season. Wine is a green, 750ml standard wine bottle, with a dravoke screw top seal. We can pick standard colors for the screw cap to match your label design.
Beverages
Adults 21 to 70 years old. A hot spiced wine, served warm, about the temperature of hot chocolate at holiday parties and family gatherings. It also can be given as a "Christmas gift" to friends, family and holiday workers.
Front label 3 1/2" wide by 4 1/2" tall max size. Back label 3" wide by 4 1/2" tall max size. Some legal text will need to be added after the winning design is selected for the back label. The following text should be incorporated on either the front or back label "Warm Mulled Wine, a light table wine with honey, unfermented cider lemon juices and spices." Also "SERVE WARM but do not boil" Also "Alcohol 9% by volume". On the back label will need to add a UPC number too along with the "GOVERNMENT WARNING"

```html
<!DOCTYPE html>
<html lang="en">
<head>
<meta charset="utf-8">
<title>Yuletide Pour – Hot Spiced Wine Label</title>
<link href="https://fonts.googleapis.com/css2?family=Cinzel:wght@400;700&family=Great+Vibes&family=Playfair+Display:wght@700&family=Libre+Baskerville&display=swap" rel="stylesheet">
<style>
  :root {
    --page: #ffffff;
    --gold-light: #e8cf9a;
    --gold-mid: #c9a263;
    --gold-dark: #9d7535;
    --red-bright: #f0342c;
    --red-mid: #cf1a1c;
    --red-deep: #8e0a10;
    --wine-panel: #2b0b0e;
    --cream: #fff6e6;
    --yellow: #ffe45a;
    --white: #ffffff;
  }
  * { margin: 0; padding: 0; box-sizing: border-box; }
  html, body { width: 1200px; height: 749px; overflow: hidden; background: var(--page); }
  .canvas { position: relative; width: 1200px; height: 749px; }

  .label {
    position: absolute; left: 372px; top: 79px; width: 456px; height: 600px;
    background: linear-gradient(135deg, var(--gold-dark) 0%, var(--gold-light) 35%, var(--gold-mid) 60%, var(--gold-light) 80%, var(--gold-dark) 100%);
  }

  .hero {
    position: absolute; left: 29px; top: 17px; width: 410px; height: 354px; overflow: hidden;
  }
  .hero-art {
    position: absolute; inset: 0;
    background:
      radial-gradient(circle at 30% 70%, rgba(255,120,110,0.55) 0 8%, transparent 22%),
      radial-gradient(circle at 70% 65%, rgba(255,90,80,0.45) 0 10%, transparent 25%),
      radial-gradient(ellipse at 50% 15%, rgba(255,200,150,0.35), transparent 45%),
      radial-gradient(ellipse at 50% 55%, var(--red-bright) 0%, var(--red-mid) 50%, var(--red-deep) 100%);
  }
  .hero-title {
    position: absolute; left: 0; right: 0; top: 160px; text-align: center;
    font-family: "Cinzel", serif; font-weight: 700; font-size: 32px; line-height: 1;
    color: var(--cream); text-shadow: 0 1px 3px rgba(80,0,0,0.5);
  }
  .hero-title .cap { font-size: 41px; }
  .hero-sub {
    position: absolute; left: 0; right: 0; top: 300px; text-align: center;
    font-family: "Playfair Display", serif; font-weight: 700; font-size: 17px; color: var(--yellow);
  }

  .rule { position: absolute; left: 36px; right: 36px; height: 2px; background: var(--white); }
  .rule.top { top: 380px; }
  .rule.bottom { top: 442px; }
  .product-name {
    position: absolute; left: 0; right: 0; top: 385px; text-align: center;
    font-family: "Great Vibes", cursive; font-weight: 400; font-size: 50px; color: var(--white); line-height: 54px;
  }

  .info-panel {
    position: absolute; left: 29px; top: 456px; width: 410px; height: 108px; background: var(--wine-panel);
  }
  .serve {
    position: absolute; left: 0; right: 0; top: 24px; text-align: center;
    font-family: "Cinzel", serif; font-size: 16px; letter-spacing: 6px; color: var(--cream);
  }
  .serve sup { font-family: "Libre Baskerville", serif; font-size: 5px; letter-spacing: 0; vertical-align: 9px; }
  .description {
    position: absolute; left: 90px; width: 222px; top: 72px; text-align: right;
    font-family: "Libre Baskerville", serif; font-size: 7.5px; line-height: 1.5; color: var(--cream);
  }
  .abv {
    position: absolute; right: 14px; top: 77px;
    font-family: "Libre Baskerville", serif; font-size: 9px; color: var(--cream);
  }
</style>
</head>
<body>
<main class="canvas">
  <article class="label">
    <section class="hero">
      <div class="hero-art" role="img" aria-label="Festive red bokeh background with golden sparkles and snowflakes"></div>
      <h1 class="hero-title"><span class="cap">H</span>OT <span class="cap">S</span>PICED <span class="cap">W</span>INE</h1>
      <p class="hero-sub">Unfermented Cider Lemon Juices And Spices</p>
    </section>
    <div class="rule top"></div>
    <h2 class="product-name">Yuletide Pour</h2>
    <div class="rule bottom"></div>
    <section class="info-panel">
      <p class="serve">SERVE WARM<sup>but do not boil</sup></p>
      <p class="description">Warm Mulled Wine, a light table wine with honey, unfermented cider lemon juices and spices.</p>
      <p class="abv">Alcohol 9%</p>
    </section>
  </article>
</main>
</body>
</html>
```